BOLD & MINIMALIST DESIGN NEEDED

We want a very bold but minimalistic business card design that is impactful and utilizes both sides of the business card. Our current logo is included for your use.

We want bold fonts and good use of negative space. We don't want the logo to overpower the design.

Target Market(s)

Professionals who are building new commercial buildings.

Industry/Entity Type

Construction

Contact Information for Business Card

Name, Title, email, office phone, cell phone, website

Font styles to use
Serif
Sans Serif

Requirements
Must have
• Bold design!

```html
<!DOCTYPE html>
<html lang="en">
<head>
<meta charset="utf-8">
<title>Ridgecrest Business Card</title>
<link href="https://fonts.googleapis.com/css2?family=Montserrat:wght@400;500;600;700;800;900&display=swap" rel="stylesheet">
<style>
  :root {
    --bg: #2b2e33;
    --card-white: #fbfbf9;
    --ink: #111111;
    --green: #7cc242;
    --green-deep: #6cb032;
    --white: #ffffff;
  }
  html, body {
    margin: 0;
    padding: 0;
    width: 1200px;
    height: 1200px;
    overflow: hidden;
    background: var(--bg);
    font-family: "Montserrat", Arial, sans-serif;
  }
  .canvas {
    position: relative;
    width: 1200px;
    height: 1200px;
  }
  .card {
    position: absolute;
    left: 160px;
    width: 880px;
    height: 500px;
    border-radius: 34px;
    overflow: hidden;
    box-shadow: 0 14px 30px rgba(0,0,0,0.35);
  }
  .card-front { top: 70px; background: var(--card-white); }
  .card-back { top: 630px; background: var(--green); }

  .front-bands { position: absolute; inset: 0; }

  .identity {
    position: absolute;
    left: 62px;
    top: 54px;
    color: var(--ink);
  }
  .person-name {
    margin: 0;
    font-size: 30px;
    font-weight: 600;
    letter-spacing: 0.5px;
  }
  .person-title {
    margin: 4px 0 0;
    font-size: 19px;
    font-weight: 500;
    color: var(--green);
  }
  .title-rule {
    width: 250px;
    height: 3px;
    background: var(--ink);
    margin: 8px 0 26px;
  }
  .contact-list {
    margin: 0;
    padding: 0;
    list-style: none;
    font-size: 17px;
    line-height: 1.4;
    font-weight: 500;
  }
  .contact-label { color: var(--green); margin-right: 4px; }
  .address-label { color: var(--green); }

  .brand {
    position: absolute;
    left: 470px;
    top: 178px;
    display: flex;
    align-items: center;
    gap: 14px;
  }
  .brand-mark {
    width: 30px;
    height: 30px;
    background: var(--green);
  }
  .brand-name {
    font-size: 50px;
    font-weight: 900;
    color: var(--ink);
    letter-spacing: 0.5px;
  }

  .correspondence {
    position: absolute;
    left: 530px;
    top: 290px;
    font-size: 19px;
    font-weight: 500;
    line-height: 1.35;
    color: var(--ink);
  }
  .correspondence-label { color: var(--green); font-weight: 600; }

  .back-pattern {
    position: absolute;
    inset: 0;
    background: radial-gradient(ellipse at 50% 45%, #86c94f 0%, var(--green) 70%);
  }
  .back-brand {
    position: absolute;
    left: 560px;
    top: 360px;
    display: flex;
    align-items: center;
    gap: 10px;
  }
  .back-brand-mark {
    width: 18px;
    height: 18px;
    background: var(--white);
  }
  .back-brand-name {
    font-size: 28px;
    font-weight: 900;
    color: var(--white);
  }
</style>
</head>
<body>
<main class="canvas">

  <section class="card card-front" aria-label="Business card front">
    <svg class="front-bands" width="880" height="500" viewBox="0 0 880 500" aria-hidden="true">
      <polygon points="0,430 380,430 372,444 0,444" fill="var(--ink)"/>
      <polygon points="418,418 880,418 880,468 392,468" fill="var(--green)"/>
    </svg>

    <div class="identity">
      <h1 class="person-name">YOUR NAME HERE</h1>
      <p class="person-title">FOUNDER / DIRECTOR</p>
      <div class="title-rule"></div>
      <ul class="contact-list">
        <li><span class="contact-label">PHONE</span>(555) 014 2200</li>
        <li><span class="contact-label">FAX</span>(555) 014 2201</li>
        <li>info@ridgecrest-db.com</li>
        <li class="address-label">PHYSICAL ADDRESS :</li>
        <li>1420 CEDAR HOLLOW RD.</li>
        <li>FERNBROOK, GA 30099</li>
      </ul>
    </div>

    <div class="brand">
      <span class="brand-mark"></span>
      <span class="brand-name">RIDGECREST</span>
    </div>

    <div class="correspondence">
      <div class="correspondence-label">CORRESPONDENCE :</div>
      <div>1420 CEDAR HOLLOW RD.</div>
      <div>FERNBROOK, GA 30099</div>
    </div>
  </section>

  <section class="card card-back" aria-label="Business card back">
    <div class="back-pattern" role="img" aria-label="Faint tone-on-tone repeat of the company emblem across the green field"></div>
    <div class="back-brand">
      <span class="back-brand-mark"></span>
      <span class="back-brand-name">RIDGECREST</span>
    </div>
  </section>

</main>
</body>
</html>
```